Ward Compass Business Card Design*

We need a business card design for our company Ward Compass. Our company is specialized in providing online consulting services regarding medical institutions, hospitals and doctors. We work with patients worldwide looking to choose between healthcare providers. We have a website you may use as a reference, where we list doctors and clinics worldwide. So we target Medical providers as well as patients worldwide.
Target Market(s)
Medical Providers and patients around the world
Industry/Entity Type
Medical
Contact Information for Business Card
Salma Derkaoui
CEO
+90 612 348 2071
info@wardcompass-example.com
www.wardcompass-example.com
14 Annakhil 3 H.R.B. Rabat, Morocco
Requirements
Must have
- Company logo/name on one full side, personal info and smaller logo and company name on the other side.
Nice to have
- Smart and elegant design

```html
<!DOCTYPE html>
<html lang="en">
<head>
<meta charset="utf-8">
<title>Ward Compass Business Card</title>
<link rel="stylesheet" href="https://fonts.googleapis.com/css2?family=Lato:wght@400;700;900&display=swap">
<style>
  :root {
    --navy: #163a68;
    --grey: #7b7d80;
    --rule: #7f98b6;
    --paper: #ffffff;
    --stage: #3a3b3e;
    --text: #505256;
  }
  * { box-sizing: border-box; margin: 0; padding: 0; }
  html, body { width: 1200px; height: 900px; overflow: hidden; }
  body {
    background: var(--stage);
    font-family: "Lato", sans-serif;
    display: flex;
    flex-direction: column;
    align-items: center;
    justify-content: center;
    gap: 40px;
  }
  .card {
    width: 600px;
    height: 343px;
    border-radius: 26px;
    position: relative;
    overflow: hidden;
  }
  .card-front {
    background: var(--navy);
    display: flex;
    align-items: center;
    justify-content: center;
    gap: 18px;
  }
  .brand-mark {
    width: 46px; height: 46px;
    border-radius: 50%;
    flex: none;
  }
  .card-front .brand-mark { background: var(--paper); }
  .brand-name {
    font-family: "Lato", sans-serif;
    font-weight: 700;
    letter-spacing: 0.06em;
    text-transform: uppercase;
  }
  .card-front .brand-name { color: var(--paper); font-size: 38px; }

  .card-back { background: var(--paper); }
  .back-brand {
    position: absolute; left: 40px; top: 58px;
    display: flex; align-items: center; gap: 12px;
  }
  .card-back .brand-mark { width: 34px; height: 34px; background: var(--navy); }
  .card-back .brand-name { color: var(--navy); font-size: 26px; }

  .person {
    position: absolute; right: 40px; top: 52px;
    text-align: right; color: var(--navy);
  }
  .person-name { font-weight: 900; font-size: 30px; line-height: 1.1; }
  .person-role { font-weight: 900; font-size: 15px; margin-top: 2px; }

  .divider {
    position: absolute; left: 40px; right: 40px; top: 150px;
    height: 1px; background: var(--rule);
  }
  .address {
    position: absolute; right: 40px; top: 168px;
    text-align: right; color: var(--text);
    font-size: 15px; line-height: 1.5;
  }
  .contacts {
    position: absolute; left: 40px; bottom: 34px;
    list-style: none; color: var(--text); font-size: 15px;
  }
  .contacts li { display: flex; align-items: center; gap: 12px; line-height: 1.9; }
  .contacts svg { width: 16px; height: 16px; flex: none; }
</style>
</head>
<body>
  <section class="card card-front" aria-label="Card front">
    <span class="brand-mark"></span>
    <span class="brand-name">Ward Compass</span>
  </section>

  <section class="card card-back" aria-label="Card back">
    <div class="back-brand">
      <span class="brand-mark"></span>
      <span class="brand-name">Ward Compass</span>
    </div>

    <div class="person">
      <p class="person-name">Salma Derkaoui</p>
      <p class="person-role">CEO</p>
    </div>

    <div class="divider"></div>

    <p class="address">14 Annakhil 3 H.R.B.<br>Rabat, Morocco</p>

    <ul class="contacts">
      <li>
        <svg viewBox="0 0 16 16" aria-hidden="true"><path fill="#163a68" d="M3.6 1.5l2.3 2.6-1.3 1.7c.9 2 2.5 3.6 4.5 4.5l1.7-1.3 2.6 2.3-1.3 2.2c-5.3-.4-9.6-4.7-10-10z"/></svg>
        +90 612 348 2071
      </li>
      <li>
        <svg viewBox="0 0 16 16" aria-hidden="true"><rect x="1" y="3" width="14" height="10" fill="#163a68"/><path d="M1 3l7 6 7-6" fill="none" stroke="#fff" stroke-width="1.2"/></svg>
        info@wardcompass-example.com
      </li>
      <li>
        <svg viewBox="0 0 16 16" aria-hidden="true"><g fill="none" stroke="#163a68" stroke-width="1.3"><circle cx="8" cy="8" r="6.5"/><ellipse cx="8" cy="8" rx="3" ry="6.5"/><path d="M1.5 8h13M2.5 5h11M2.5 11h11"/></g></svg>
        www.wardcompass-example.com
      </li>
    </ul>
  </section>
</body>
</html>
```